Boracay Wedding Invitation Design

Hello, We would like a wedding invitation design for our wedding in Boracay. We would like it somewhat in the form of a boarding pass with beachy fresh colours, possibly a nice Boracay beach in the background Double sided with an envelope design to match. Maybe something simple on the envelope like a nice picture in the bottom left corner of a shell on a beach or something similar.

I would also like on the opposite side of the invite to be an "information sheet" with a matching beach design

The text files for both sides are included and i have also included 2 designs that i thought looked nice and are similar to what we are after.
Updates

Hello, I have updated the brief to be more specific with text files and images to make it easier for you. Thank you :)

Industry/Entity Type

Wedding

Font styles to use
Decorative
Script

Colors
fbee3d
33a6d7
33b8a4
fbf289
85cae6
ffffff

Requirements
Must have
• I would like to have this quote somewhere on the invitation
• This day I will marry my best friend,
• the one I laugh with,
• live for,
• dream with,
• love
• Owen & Marisa
• Request the pleasure of your company to celebrate their wedding
• On Friday the 17th March 2017
• at
• Velunda Grand Suites
• Boracay, Philippines
• Ceremony begins at 3.00pm
• RSVP
• Owen 0431907254
• Marisa 0417283649
• by
• 17th Jan 2016
• Dress: Beach Formal
• For the "information sheet"
• There will be a 5% discount on rooms booked at the Velunda under the event Owen & Marisa Wedding. The resort has a total of 24 rooms it would be nice if the majority of guests could stay at the resort from the night before until the night after the wedding but if you choose to stay elsewhere on the island there are plenty of other places to stay for cheaper and everything is fairly close as its a small island.
• We have currently blocked room stay for a short period of time so our guests can book rooms. If you choose to do so please email reservations@velundastays.example. Once rooms become available to the public again, towards the end of Jan, it will be first come first served basis. The resort is very popular so im assuming once this happens the rooms will be booked out.
• If you would like to check out the resort itself the website is www.velundagrand-isle.example
• We know its a fair distance to travel but we would really love to see you all there to celebrate and maybe even enjoy a small holiday while your here its a beautiful part of the world.
• If anyone has any questions please feel free to contact Owen on 0431907254
Nice to have
• A nice picture of a Boracay beach in the background would be nice

```html
<!DOCTYPE html>
<html lang="en">
<head>
<meta charset="utf-8">
<title>Owen &amp; Marisa – Boarding Pass Wedding Invitation</title>
<link rel="stylesheet" href="https://fonts.googleapis.com/css2?family=Great+Vibes&family=Anonymous+Pro:wght@400;700&family=Share+Tech+Mono&family=Oswald:wght@400;500&family=PT+Sans+Narrow:wght@400;700&display=swap">
<style>
  :root {
    --page: #ece8e1;
    --sky-blue: #33a6d7;
    --script-blue: #4cc1ee;
    --pill-blue: #3fb6ea;
    --pale-blue: #a9def1;
    --mid-blue: #5cc3ec;
    --deep-blue: #3bb0e4;
    --sand: #e6e0d5;
    --sand-warm: #e8dcc4;
    --cream: #fbf4e3;
    --ink: #1c1c1c;
    --ink-soft: #333;
    --white: #ffffff;
    --dash: #a9a6a0;
  }
  * { box-sizing: border-box; margin: 0; padding: 0; }
  html, body { width: 1200px; height: 1050px; overflow: hidden; }
  body { background: var(--page); position: relative; font-family: "PT Sans Narrow", sans-serif; color: var(--ink); }

  .card { position: absolute; left: 50px; width: 1105px; height: 485px; overflow: hidden; }
  .card--front { top: 27px; }
  .card--back { top: 532px; }

  .beach-backdrop { position: absolute; inset: 0; }
  .card--front .beach-backdrop {
    background: linear-gradient(180deg, #9fd3d8 0%, #cfe3df 14%, var(--sand) 34%, #e3ddd1 70%, #ddd6c8 100%);
  }
  .card--back .beach-backdrop {
    background: linear-gradient(90deg, #8ccdd4 0%, #b9ddd7 18%, var(--sand-warm) 40%, #eadfcb 75%, #e4d7bf 100%);
  }

  /* front */
  .ticket-panel { position: absolute; left: 5px; top: 10px; width: 1088px; height: 463px; border-radius: 14px; background: rgba(255,255,255,0.32); }
  .dash-v, .dash-h { position: absolute; border-color: var(--dash); border-style: dashed; border-width: 0; }
  .dash-v { border-left-width: 1.5px; }
  .dash-h { border-top-width: 1.5px; }
  .dash-v--stub { left: 365px; top: 10px; height: 463px; }
  .dash-h--details { left: 365px; top: 220px; width: 728px; }
  .dash-v--details { left: 630px; top: 220px; height: 253px; }

  .stub-label { position: absolute; left: -168px; top: 215px; width: 410px; height: 50px; transform: rotate(-90deg);
    font-family: "Share Tech Mono", monospace; color: var(--ink-soft); line-height: 22px; }
  .stub-label__title { font-size: 20px; letter-spacing: 5px; padding-left: 92px; }
  .stub-label__sub { font-size: 17px; letter-spacing: 2px; }

  .vow-quote { position: absolute; left: 70px; top: 53px; width: 290px; text-align: center;
    font-family: "Anonymous Pro", monospace; font-size: 19px; line-height: 20.8px; color: var(--ink); letter-spacing: 0.5px; }

  .date-day { position: absolute; left: 88px; top: 150px; width: 240px; text-align: center;
    font-family: "PT Sans Narrow", sans-serif; font-weight: 700; font-size: 285px; line-height: 1; color: var(--sky-blue);
    letter-spacing: -10px; transform: scaleX(0.78); transform-origin: center top;
    text-shadow: 6px 8px 10px rgba(0,0,0,0.18); }
  .date-month { position: absolute; left: 100px; top: 392px; width: 240px; text-align: center;
    font-family: "PT Sans Narrow", sans-serif; font-weight: 700; font-size: 42px; line-height: 48px; color: var(--white);
    text-shadow: 2px 3px 5px rgba(0,0,0,0.45); }

  .couple-names { position: absolute; left: 470px; top: 12px; width: 550px; text-align: center;
    font-family: "Great Vibes", cursive; font-weight: 400; font-size: 74px; line-height: 1.1; color: var(--script-blue); }
  .invite-line { position: absolute; left: 400px; top: 101px; width: 680px; text-align: center;
    font-family: "Anonymous Pro", monospace; font-weight: 700; font-size: 26px; line-height: 30px; letter-spacing: 2.5px; }
  .date-pill { position: absolute; left: 542px; top: 166px; width: 406px; height: 44px; border-radius: 22px;
    background: var(--pill-blue); color: var(--white); text-align: center;
    font-family: "PT Sans Narrow", sans-serif; font-size: 29px; line-height: 44px; }

  .venue-block { position: absolute; left: 383px; top: 230px; width: 245px; }
  .venue-block__heading { font-family: "Oswald", sans-serif; font-size: 19px; line-height: 26px; letter-spacing: 1px; color: var(--ink); }
  .venue-block__name { margin-top: 4px; font-family: "Share Tech Mono", monospace; font-size: 24px; line-height: 38px; letter-spacing: -0.3px; white-space: nowrap; }
  .rsvp { margin-top: 6px; font-family: "Anonymous Pro", monospace; font-size: 20px; line-height: 21.5px; letter-spacing: 0.5px; }

  .beach-photo--front { position: absolute; left: 688px; top: 231px; width: 387px; height: 197px;
    background: linear-gradient(180deg, #3d8fd8 0%, #8cc6ee 45%, #bfe4f2 58%, #3fc6c9 66%, #8fdcd3 76%, #f4f1ea 86%, #eae6dc 100%); }
  .attire { position: absolute; left: 690px; top: 441px; width: 384px; text-align: center;
    font-family: "Anonymous Pro", monospace; font-size: 19px; letter-spacing: 0.5px; }

  /* back */
  .rotated { position: absolute; transform: rotate(-90deg); }
  .info-tab { left: -95px; top: 173px; width: 390px; height: 140px; background: var(--cream);
    border-radius: 10px 10px 46px 46px / 10px 10px 30px 30px; padding: 16px 30px; box-shadow: 2px 3px 8px rgba(0,0,0,0.15); }
  .info-tab__title { font-family: "PT Sans Narrow", sans-serif; font-size: 38px; line-height: 42px; color: var(--mid-blue); }
  .info-tab__detail { font-family: "PT Sans Narrow", sans-serif; font-size: 29px; line-height: 28px; color: var(--ink); padding-left: 36px; }

  .info-copy { font-family: "PT Sans Narrow", sans-serif; font-size: 17px; line-height: 24.5px; color: var(--ink); }
  .info-copy--stay { left: 106px; top: 164px; width: 408px; height: 176px; }
  .info-box { border-radius: 16px; padding: 10px 12px 10px 16px; }
  .info-box--booking { left: 286.5px; top: 156.5px; width: 435px; height: 172px; background: var(--pale-blue); }
  .info-box--website { left: 418.5px; top: 211.5px; width: 435px; height: 62px; background: var(--mid-blue); }
  .info-box--welcome { left: 527.5px; top: 177.5px; width: 435px; height: 130px; background: var(--deep-blue); }

  .beach-photo--back { position: absolute; left: 840px; top: 34px; width: 237px; height: 420px;
    border: 3px solid var(--deep-blue); border-radius: 12px;
    background: linear-gradient(90deg, #2f5a2c 0%, #5f8a4a 22%, #cfe4f0 40%, #9fd6e8 55%, #37b3c2 68%, #f0ece2 84%, #e6ddcc 100%); }

  .phone-icon { display: inline-block; width: 15px; height: 15px; vertical-align: -2px; }
</style>
</head>
<body>

<section class="card card--front" aria-label="Invitation front">
  <div class="beach-backdrop" role="img" aria-label="Soft photograph of white sand and shallow turquoise water"></div>
  <div class="ticket-panel"></div>
  <div class="dash-v dash-v--stub"></div>
  <div class="dash-h dash-h--details"></div>
  <div class="dash-v dash-v--details"></div>

  <div class="stub-label">
    <div class="stub-label__title">BOARDING PASS</div>
    <div class="stub-label__sub">OWEN &amp; MARISA WEDDING | 02.17.15</div>
  </div>

  <p class="vow-quote">This day I will marry<br>my best friend,<br>the one I laugh with,<br>live for,<br>dream with,<br>love</p>

  <div class="date-day">17</div>
  <div class="date-month">MARCH 2016</div>

  <h1 class="couple-names">Owen &amp; Marisa</h1>
  <p class="invite-line">REQUEST THE PLEASURE OF YOUR COMPANY<br>TO CELEBRATE THEIR WEDDING</p>
  <div class="date-pill">FRIDAY,&nbsp; MARCH 17, 2017 AT 3 PM</div>

  <div class="venue-block">
    <div class="venue-block__heading">CEREMONY &amp; RECEPTION</div>
    <div class="venue-block__name">VELUNDA GRAND SUITES<br>BORACAY ISLAND,<br>PHILIPPINES</div>
    <div class="rsvp">RSVP<br>Owen 0431907254<br>Marisa 0417283649<br>by 17th Jan 2016</div>
  </div>

  <div class="beach-photo--front" role="img" aria-label="Photograph of leaning palm trees over a white beach with turquoise sea and sailboats"></div>
  <p class="attire">Attire: Beach Formal</p>
</section>

<section class="card card--back" aria-label="Information sheet">
  <div class="beach-backdrop" role="img" aria-label="Faded photograph of shoreline and sand"></div>

  <div class="rotated info-tab">
    <div class="info-tab__title">Owen &amp; Marisa Wedding</div>
    <div class="info-tab__detail">Velunda Grand Suites<br>Boracay, Philippines<br>March 17, 2016</div>
  </div>

  <p class="rotated info-copy info-copy--stay">There will be a 5% discount on rooms booked at the Velunda under the event Owen &amp; Marisa Wedding. The resort has a total of 24 rooms it would be nice if the majority of guests could stay at the resort from the night before until the night after the wedding but if you choose to stay elsewhere on the island there are plenty of other places to stay for cheaper and everything is fairly close as its a small island.</p>

  <p class="rotated info-copy info-box info-box--booking">We have currently blocked room stay for a short period of time so our guests can book rooms. If you choose to do so please email reservations@velundastays.example. Once rooms become available to the public again, towards the end of January, it will be first come first served basis. The resort is very popular so im assuming once this happens the rooms will be booked out.</p>

  <p class="rotated info-copy info-box info-box--website">If you would like to check out the resort itself the website is www.velundagrand-isle.example</p>

  <p class="rotated info-copy info-box info-box--welcome">We know its a fair distance to travel but we would really love to see you all there to celebrate and maybe even enjoy a small holiday while your here its a beautiful part of the world.- If anyone has any questions please feel free to contact Owen on <svg class="phone-icon" viewBox="0 0 16 16" aria-hidden="true"><circle cx="8" cy="8" r="7" fill="none" stroke="#1c1c1c" stroke-width="1.3"/><path d="M5.6 4.4l1.3 1.6-.8 1c.5 1 1.2 1.7 2.1 2.2l1-.8 1.6 1.3-.9 1.2c-2.5-.4-4.8-2.7-5.2-5.3z" fill="#1c1c1c"/></svg> 0431907254.</p>

  <div class="beach-photo--back" role="img" aria-label="Photograph of palm fronds framing a long white beach and blue sea"></div>
</section>

</body>
</html>
```